Business Card & Letterhead Design

We a financial advice company based in Australia. We provide advice to wealthy farmers.

We are changing our business name FROM Palomar Financial TO Bluegate Wealth and we need a new letterhead and double sided business card design

Attached is designs from our previous branding (Palomar Financial) as it includes all the details we require on the new Bluegate Wealth business cards and letterhead.

```html
<!DOCTYPE html>
<html lang="en">
<head>
<meta charset="utf-8">
<title>Bluegate Wealth – Business Card</title>
<link rel="stylesheet" href="https://fonts.googleapis.com/css2?family=Cinzel:wght@400&family=Mulish:wght@400;600&display=swap">
<style>
  :root {
    --backdrop: #a6a6a6;
    --paper: #f7f7f7;
    --charcoal: #47484a;
    --ink: #3a3a3c;
    --muted: #8a8a8c;
    --gilt: #c9a21a;
  }
  * { margin: 0; padding: 0; box-sizing: border-box; }
  html, body { width: 1200px; height: 857px; overflow: hidden; }
  body {
    background: var(--backdrop);
    font-family: "Mulish", sans-serif;
    color: var(--ink);
    position: relative;
  }
  .card {
    position: absolute;
    top: 258px;
    width: 540px;
    height: 310px;
    border-bottom: 3px solid var(--gilt);
    box-shadow: 0 10px 24px rgba(0,0,0,0.22);
    overflow: hidden;
  }
  .card-front { left: 50px; background: var(--paper); }
  .card-back { left: 610px; background: var(--charcoal); }

  .band-bottom {
    position: absolute; left: 0; right: 0; bottom: 0;
    height: 22px; background: var(--charcoal);
  }
  .band-corner {
    position: absolute; right: 0; bottom: 0;
    width: 64px; height: 70px; background: var(--charcoal);
  }

  .brand {
    position: absolute; left: 34px; top: 40px;
    display: flex; align-items: center; gap: 14px;
  }
  .brand-circle {
    width: 46px; height: 46px; border-radius: 50%;
    border: 2px solid var(--ink); flex: none;
  }
  .brand-name {
    font-family: "Cinzel", serif;
    font-size: 25px; letter-spacing: 1px; line-height: 1;
    color: var(--ink);
  }
  .brand-tagline {
    font-family: "Mulish", sans-serif;
    font-size: 9px; letter-spacing: 4.2px;
    color: var(--muted); margin-top: 5px;
  }

  .contact {
    position: absolute; left: 34px; top: 132px;
    font-size: 12.5px; line-height: 1.45;
  }
  .contact-address { margin-bottom: 10px; }
  .contact-list { list-style: none; }
  .contact-list li { display: flex; align-items: center; gap: 9px; }
  .contact-list svg { width: 11px; height: 11px; fill: var(--ink); flex: none; }

  .person {
    position: absolute; right: 92px; top: 104px; text-align: left;
  }
  .person-name { font-size: 17px; font-weight: 600; letter-spacing: 0.5px; }
  .person-role { font-size: 12px; color: #555; margin-top: 2px; }

  .back-pattern { position: absolute; inset: 0; }
</style>
</head>
<body>

<section class="card card-front" aria-label="Business card front">
  <div class="brand">
    <span class="brand-circle"></span>
    <div>
      <div class="brand-name">Bluegate Wealth</div>
      <div class="brand-tagline">STRATEGIC FINANCIAL ADVICE</div>
    </div>
  </div>

  <div class="contact">
    <p class="contact-address">P/18 Calder Ridge Road<br>Wattle Vale, NSW 2794</p>
    <ul class="contact-list">
      <li><svg viewBox="0 0 12 12"><path d="M2.5 1l2 2.2-1 1.3c.7 1.5 1.7 2.5 3 3.1l1.2-1 2.3 1.9-1 1.9C5.5 10 2 6.6 1.4 2.1z"/></svg>+61 2 6300 4418</li>
      <li><svg viewBox="0 0 12 12"><path d="M3 0.5h6v11H3zM4 1.5v8h4v-8z"/></svg>+61 412 557 903</li>
      <li><svg viewBox="0 0 12 12"><path d="M0.5 2.5h11v7h-11zM1.5 3.3l4.5 3.3 4.5-3.3z"/></svg>daniel.hartley@bluegatewealth.au</li>
      <li><svg viewBox="0 0 12 12"><circle cx="6" cy="6" r="5.3"/></svg>www.bluegatewealth.au</li>
    </ul>
  </div>

  <div class="person">
    <div class="person-name">DANIEL HARTLEY</div>
    <div class="person-role">Operational Manager</div>
  </div>

  <div class="band-corner"></div>
  <div class="band-bottom"></div>
</section>

<section class="card card-back" aria-label="Business card back">
  <div class="back-pattern" role="img" aria-label="Blind-embossed repeating brand monogram pattern on charcoal stock"></div>
</section>

</body>
</html>
```